Pelbrook Business Cards

Create new business cards with the details below.

Aaron Velst
Director

MB: +61 412 563 904
PH: 1300 417 639
Email: aaron.velst@pelbrook.com.au
Address: 27C Marlow Parade, Kelbridge VIC 3094 Australia
Website: www.pelbrook.com.au

Target Market(s)

Other business

Industry/Entity Type

Business

Requirements
Must have
• must be clean looking

```html
<!DOCTYPE html>
<html lang="en">
<head>
<meta charset="utf-8">
<title>Pelbrook Business Cards</title>
<link href="https://fonts.googleapis.com/css2?family=Open+Sans:wght@400;600;700&display=swap" rel="stylesheet">
<style>
  :root {
    --bg: #d9d9d9;
    --paper: #ffffff;
    --lime: #9ccb3b;
    --ink: #111111;
    --dark: #231f20;
  }
  * { margin: 0; padding: 0; box-sizing: border-box; }
  html, body { width: 1200px; height: 1046px; overflow: hidden; }
  body {
    background: var(--bg);
    font-family: "Open Sans", Arial, sans-serif;
    position: relative;
  }
  .card {
    position: absolute;
    top: 178px;
    width: 420px;
    height: 690px;
    background: var(--paper);
    box-shadow: 0 6px 18px rgba(0,0,0,0.18);
    overflow: hidden;
  }
  .card--front { left: 140px; }
  .card--back { left: 640px; }

  .edge-band {
    position: absolute; left: 0; right: 0;
    height: 34px;
    background: var(--lime);
  }
  .edge-band--top { top: 0; border-bottom: 7px solid var(--ink); }
  .edge-band--bottom { bottom: 0; border-top: 7px solid var(--ink); }

  .brand {
    position: absolute; left: 0; right: 0;
    display: flex; align-items: center; justify-content: center; gap: 14px;
  }
  .card--front .brand { top: 318px; }
  .card--back .brand { top: 168px; }
  .brand-square {
    width: 34px; height: 34px;
    background: var(--lime);
  }
  .brand-name {
    font-weight: 700;
    font-size: 42px;
    letter-spacing: 1px;
    color: var(--dark);
    line-height: 1;
  }

  .role-band {
    position: absolute; left: 0; right: 0; top: 372px;
    height: 40px;
    background: var(--lime);
    display: flex; align-items: center;
    padding-left: 34px;
    font-size: 18px;
    color: var(--dark);
  }
  .role-band .person { font-weight: 700; }
  .role-band .divider { margin: 0 10px; font-weight: 400; }
  .role-band .title { font-weight: 400; }

  .contact-panel {
    position: absolute; left: 0; right: 0; top: 412px; bottom: 0;
    background: var(--ink);
    padding: 30px 34px;
  }
  .contact-list { list-style: none; }
  .contact-item {
    display: flex; align-items: flex-start; gap: 14px;
    color: var(--lime);
    font-size: 17px;
    line-height: 1.35;
    margin-bottom: 12px;
  }
  .contact-item svg { flex: none; width: 20px; height: 20px; margin-top: 2px; }
</style>
</head>
<body>

  <section class="card card--front" aria-label="Card front">
    <div class="edge-band edge-band--top"></div>
    <div class="brand">
      <span class="brand-square"></span>
      <span class="brand-name">PELBROOK</span>
    </div>
    <div class="edge-band edge-band--bottom"></div>
  </section>

  <section class="card card--back" aria-label="Card back">
    <div class="brand">
      <span class="brand-square"></span>
      <span class="brand-name">PELBROOK</span>
    </div>

    <div class="role-band">
      <span class="person">Aaron Velst</span>
      <span class="divider">|</span>
      <span class="title">Director</span>
    </div>

    <div class="contact-panel">
      <ul class="contact-list">
        <li class="contact-item">
          <svg viewBox="0 0 20 20" aria-hidden="true"><circle cx="10" cy="10" r="10" fill="#9ccb3b"/><rect x="7" y="4.5" width="6" height="11" rx="1" fill="#111"/><rect x="8" y="6" width="4" height="6.5" fill="#9ccb3b"/></svg>
          <span>+61 412 563 904</span>
        </li>
        <li class="contact-item">
          <svg viewBox="0 0 20 20" aria-hidden="true"><circle cx="10" cy="10" r="10" fill="#9ccb3b"/><path d="M7 5c1 0 1.6 2 1.6 2.6 0 .6-.8 1-.8 1.4.4 1.3 1.7 2.6 3 3 .4 0 .8-.8 1.4-.8.6 0 2.6.6 2.6 1.6 0 1-1 2-2 2C9.5 14.8 5.2 10.5 5 7c0-1 1-2 2-2z" fill="#111"/></svg>
          <span>1300 417 639</span>
        </li>
        <li class="contact-item">
          <svg viewBox="0 0 20 20" aria-hidden="true"><rect x="1" y="4" width="18" height="12" fill="#9ccb3b"/><path d="M1 4l9 7 9-7" fill="none" stroke="#111" stroke-width="1.5"/></svg>
          <span>aaron.velst@pelbrook.com.au</span>
        </li>
        <li class="contact-item">
          <svg viewBox="0 0 20 20" aria-hidden="true"><circle cx="10" cy="10" r="9" fill="#9ccb3b"/><path d="M1 10h18M10 1c-3 3-3 15 0 18M10 1c3 3 3 15 0 18" fill="none" stroke="#111" stroke-width="1.2"/></svg>
          <span>www.pelbrook.com.au</span>
        </li>
        <li class="contact-item">
          <svg viewBox="0 0 20 20" aria-hidden="true"><path d="M10 1a6.5 6.5 0 0 0-6.5 6.5C3.5 12 10 19 10 19s6.5-7 6.5-11.5A6.5 6.5 0 0 0 10 1z" fill="#9ccb3b"/><circle cx="10" cy="7.5" r="2.5" fill="#111"/></svg>
          <span>27C Marlow Parade,<br>Kelbridge, VIC 3094</span>
        </li>
      </ul>
    </div>
  </section>

</body>
</html>
```